BSWC Steadwell Foot Health Care

Steadwell Foot Health Care guarantees to treat your foot problems in one visit or we will provide a free treatment session to you until you are completely satisfied.

10% discount for all new patients!

Mobile foot care at home!

Professional and fully qualified and insured foot health care practitioner

Expert advice

How to care for your feet

Treatments; Diabetic foot health, Corns, Callouses, Fungal Infections, Verrucas, Cracked Heels, Ingrowing Toenails, Ball of foot pain and Heel pain.

```html
<!DOCTYPE html>
<html lang="en">
<head>
<meta charset="utf-8">
<title>Steadwell Foot Health Care – Flyer</title>
<link rel="stylesheet" href="https://fonts.googleapis.com/css2?family=Roboto+Condensed:wght@400;700&family=Lato:wght@400;700&family=Montserrat:wght@700&display=swap">
<style>
  :root{
    --green:#7cc143;
    --green-dark:#5fa82c;
    --blue-light:#7fd0f2;
    --blue-deep:#2f8fc4;
    --ink:#231f20;
    --charcoal:#3b3b3d;
    --white:#ffffff;
  }
  *{margin:0;padding:0;box-sizing:border-box}
  html,body{width:907px;height:1200px;overflow:hidden;background:var(--white)}
  .flyer{position:relative;width:907px;height:1200px;background:var(--white);overflow:hidden;font-family:'Lato',sans-serif;color:var(--ink)}
  .flyer__shapes{position:absolute;inset:0;width:907px;height:1200px}

  .brand{position:absolute;right:52px;top:44px;text-align:right;font-family:'Roboto Condensed',sans-serif;font-weight:700}
  .brand__name{display:block;color:var(--green);font-size:60px;line-height:1;letter-spacing:1px}
  .brand__tag{display:block;color:var(--ink);font-size:31px;line-height:1.2;margin-top:6px}

  .photo-circle{position:absolute;border-radius:50%}
  .photo-circle--treatment{left:614px;top:156px;width:286px;height:286px;border:8px solid var(--white);background:radial-gradient(circle at 55% 58%,#e6c6b0 0%,#c99b85 30%,#1f3354 64%,#142440 100%)}
  .photo-circle--feet{left:590px;top:818px;width:264px;height:264px;border:9px solid var(--green);background:radial-gradient(circle at 45% 50%,#efc4ad 0%,#d89e86 35%,#2b2b2b 68%,#111 100%)}

  .offer{position:absolute;left:523px;top:434px;width:384px;height:204px;padding:44px 0 0 32px;border-radius:0 0 0 34px;background:linear-gradient(180deg,var(--blue-light),var(--blue-deep));color:var(--white)}
  .offer__lead{font-family:'Roboto Condensed',sans-serif;font-weight:700;font-size:36px;line-height:1.05}
  .offer__line{font-family:'Roboto Condensed',sans-serif;font-weight:700;font-size:26px;color:var(--ink);line-height:1.35}
  .offer__plain{font-size:26px;color:var(--ink);line-height:1.25}
  .offer__strong{font-weight:700;font-size:26px;line-height:1.25}

  .discount{position:absolute;left:530px;top:659px;width:368px;height:96px;border-radius:8px;background:var(--green);color:var(--white);display:flex;align-items:center;padding-left:26px;font-family:'Roboto Condensed',sans-serif;font-weight:700}
  .discount__value{font-size:60px;line-height:1}
  .discount__label{writing-mode:vertical-rl;transform:rotate(180deg);font-size:15px;font-weight:400;margin:0 10px 0 4px;letter-spacing:.5px}
  .discount__text{font-size:29px;line-height:1.1}
  .discount__text strong{display:block;font-size:34px;color:var(--ink)}

  .headline{position:absolute;left:35px;top:466px;font-family:'Roboto Condensed',sans-serif;font-weight:700}
  .headline__green{display:block;color:var(--green);font-size:59px;line-height:1}
  .headline__main{display:block;color:var(--ink);font-size:55px;line-height:1.1;margin-top:8px}
  .headline__sub{display:block;font-family:'Lato',sans-serif;font-size:33px;line-height:1.2;margin-top:2px}

  .body-copy{position:absolute;left:35px;top:654px;width:404px;font-size:14.5px;line-height:1.28;text-align:justify;color:var(--ink)}
  .body-copy p + p{margin-top:5px}
  .body-copy strong{color:var(--green-dark)}

  .credentials{position:absolute;left:35px;top:868px;font-family:'Roboto Condensed',sans-serif}
  .credentials__green{display:block;color:var(--green);font-weight:700;font-size:30px;line-height:1.1}
  .credentials__plain{display:block;font-family:'Lato',sans-serif;font-size:22px;line-height:1.35}

  .cta{position:absolute;left:44px;top:1013px;font-weight:700}
  .cta__call{display:block;font-family:'Montserrat',sans-serif;color:var(--blue-light);font-size:31px;letter-spacing:1px;line-height:1}
  .cta__register{display:block;font-family:'Roboto Condensed',sans-serif;color:var(--white);font-size:51px;line-height:1.05;margin-top:10px}
  .cta__phone{display:block;font-family:'Roboto Condensed',sans-serif;color:var(--green);font-size:50px;line-height:1.05}

  .badge{position:absolute}
  .badge--register{left:372px;top:1096px;width:122px;height:64px;background:var(--white);border-radius:2px}
  .badge--alliance{left:530px;top:1073px;width:108px;height:108px;border-radius:50%;background:var(--white);border:6px solid var(--green-dark)}
</style>
</head>
<body>
<main class="flyer">
  <svg class="flyer__shapes" viewBox="0 0 907 1200" aria-hidden="true">
    <defs>
      <linearGradient id="sandGrad" x1="0" y1="0" x2="0" y2="1">
        <stop offset="0" stop-color="#c8cfd2"/>
        <stop offset=".4" stop-color="#e6d7bf"/>
        <stop offset="1" stop-color="#cdb18d"/>
      </linearGradient>
      <linearGradient id="fadeRight" x1="0" y1="0" x2="1" y2="0">
        <stop offset=".6" stop-color="#ffffff" stop-opacity="0"/>
        <stop offset="1" stop-color="#ffffff" stop-opacity="1"/>
      </linearGradient>
    </defs>
    <path d="M907 130 C870 260 860 380 800 434 L907 434 Z" fill="var(--blue-light)"/>
    <path d="M890 120 C860 230 840 300 800 360" fill="none" stroke="var(--green)" stroke-width="9"/>
    <g role="img" aria-label="Photo: bare feet walking on a sandy beach by the sea">
      <path d="M0 0 H760 V150 C700 300 560 410 380 412 C220 414 90 360 0 300 Z" fill="url(#sandGrad)"/>
      <path d="M0 0 H760 V150 C700 300 560 410 380 412 C220 414 90 360 0 300 Z" fill="url(#fadeRight)"/>
    </g>
    <path d="M0 300 C110 372 240 414 390 420 C480 424 560 418 640 406" fill="none" stroke="var(--blue-light)" stroke-width="7"/>
    <path d="M0 318 C120 400 260 440 420 444 C500 446 570 438 630 428" fill="none" stroke="var(--green)" stroke-width="16"/>
    <path d="M0 938 C260 912 560 912 907 960" fill="none" stroke="var(--blue-light)" stroke-width="6"/>
    <path d="M0 962 C260 932 560 934 907 984" fill="none" stroke="var(--green)" stroke-width="16"/>
    <path d="M0 976 C260 946 560 950 907 1000 V1200 H0 Z" fill="var(--charcoal)"/>
  </svg>

  <header class="brand">
    <span class="brand__name">STEADWELL</span>
    <span class="brand__tag">FOOT HEALTH CARE</span>
  </header>

  <div class="photo-circle photo-circle--treatment" role="img" aria-label="Photo: gloved practitioner treating a toenail"></div>

  <section class="offer">
    <p class="offer__lead">WE WILL PROVIDE</p>
    <p class="offer__line">a free treatment session</p>
    <p class="offer__plain">to you until you are</p>
    <p class="offer__strong">completely satisfied</p>
  </section>

  <section class="discount">
    <span class="discount__value">10%</span>
    <span class="discount__label">Discount</span>
    <span class="discount__text">FOR ALL NEW<strong>PATIENTS</strong></span>
  </section>

  <h1 class="headline">
    <span class="headline__green">GUARANTEES TO</span>
    <span class="headline__main">TREAT YOUR FOOT</span>
    <span class="headline__sub">PROBLEMS IN ONE VISIT</span>
  </h1>

  <div class="body-copy">
    <p>BSWC Steadwell Foot Health Care Guarantees to treat your foot problems in one visit or we will provide a free treatment session to you until you're completely satisfied. From as little as 30 per treatment session our fully qualified and insured Foot Health Care Practitioner will immediately bring you pain relief while also offering you professional expert advice on how to care for your feet and keep them looking good all year round.</p>
    <p><strong>Mobile foot care at home!</strong> Treatments: Diabetic foot health, Corns, Callouses, Fungal Infections, Verrucas, Cracked Heels, Ingrowing Toenails, Ball of foot pain and Heel pain.</p>
  </div>

  <p class="credentials">
    <span class="credentials__green">Professional and fully qualified</span>
    <span class="credentials__plain">and insured foot health care practitioner</span>
  </p>

  <div class="photo-circle photo-circle--feet" role="img" aria-label="Photo: soles of a pair of bare feet"></div>

  <footer class="cta">
    <span class="cta__call">CALL NOW</span>
    <span class="cta__register">TO REGISTER</span>
    <span class="cta__phone">07700 900418</span>
  </footer>

  <div class="badge badge--register" role="img" aria-label="Accreditation badge"></div>
  <div class="badge badge--alliance" role="img" aria-label="Membership badge"></div>
</main>
</body>
</html>
```